Tallowfern Letterheads Design

Hello, we have just upgraded this project for a guaranteed payment.

We are currently going through a re-branding exercise internally. Our logo is attached as a PDF file.

We are happy with our logo but would like to investigate how we can best apply the logo to our letterheads and compliment slips.

We are a quality printing company in England. Despite our name we are very professional and offer a personal service.

Our new website is under construction and here is a link to show you how it looks: http://tallowpress.marlwood.co.uk

The style must be professional and steer away from "tacky" otherwise it makes our company look very low budget and just a bit silly.

We would like to see elements of creativity though, so please, nothing too boring.

I have attached our new logo, there is an option for use on white or black.

Cheers
Tallowfern Team
Updates

Project Deadline Extended
Reason: We have increased the deadline due to an internal delay to things, we now have more time before we need anything to be printed.

Industry/Entity Type

Construction

Requirements
Must have
• IMPORTANT! Please do not tweak or change our logo in any way. A few designs show vast changes in the logo, this is not what we require. Please do not change the logo in any way. Thanks
Nice to have
• Classy but approachable. Elements of "quirky" would be nice to see.
Should not have
• A Tacky feel

```html
<!DOCTYPE html>
<html lang="en">
<head>
<meta charset="utf-8">
<title>Tallowfern Letterhead</title>
<link rel="stylesheet" href="https://fonts.googleapis.com/css2?family=Questrial&display=swap">
<style>
  :root {
    --ink: #171c1e;
    --paper: #ffffff;
    --brand-pink: #e5286f;
    --mist: #f3f4f5;
    --mist-edge: #ecedee;
  }
  html, body {
    margin: 0;
    padding: 0;
    overflow: hidden;
    background: var(--paper);
  }
  .letterhead {
    position: relative;
    width: 848px;
    height: 1200px;
    overflow: hidden;
    background: var(--paper);
    font-family: "Questrial", "Century Gothic", sans-serif;
  }
  .masthead {
    position: absolute;
    left: 0;
    top: 0;
    width: 848px;
    height: 190px;
    background: var(--ink);
  }
  .contact-panel {
    position: absolute;
    left: 418px;
    top: 0;
    width: 430px;
    height: 190px;
    background: var(--paper);
    border-radius: 0 0 0 70px;
  }
  .brand {
    position: absolute;
    left: 16px;
    top: 104px;
    color: var(--paper);
  }
  .brand-name {
    margin: 0;
    font-size: 42px;
    line-height: 1;
    font-weight: 400;
    letter-spacing: 0.5px;
  }
  .brand-tagline {
    margin: 10px 0 0 44px;
    font-size: 19px;
    line-height: 1;
  }
  .contact {
    position: absolute;
    right: 14px;
    top: 96px;
    margin: 0;
    text-align: right;
    color: var(--brand-pink);
    font-size: 11.5px;
    line-height: 17px;
    font-style: normal;
  }
  .contact-web {
    font-weight: 700;
  }
  .watermark {
    position: absolute;
    left: 310px;
    top: 627px;
    width: 530px;
    height: 556px;
    border-radius: 46% 40% 30% 34%;
    background: radial-gradient(ellipse at 45% 45%, var(--mist) 0%, var(--mist) 60%, var(--mist-edge) 100%);
    opacity: 0.8;
  }
</style>
</head>
<body>
  <main class="letterhead">
    <header class="masthead">
      <div class="contact-panel" role="img" aria-label="Soft white cloud shape behind the contact details"></div>
      <div class="brand">
        <h1 class="brand-name">Tallowfern</h1>
        <p class="brand-tagline">Quality Printing</p>
      </div>
      <address class="contact">
        18 Orchard Lane, Bramwell-On-The-Rise, Bramwell, Kent, TN4 7QJ •<br>
        Tel: 0207 384 2916 • <span class="contact-web">www.tallowpress.marlwood.co.uk •</span>
      </address>
    </header>
    <div class="watermark" role="img" aria-label="Faint large brand decoration"></div>
  </main>
</body>
</html>
```